Hedge Fund Business Presentation for prospective clients

We need a professional design for our PowerPoint presentation that we use to send to prospective clients for our Alternative Investments/Hedge Fund. This presentation needs to have the same verbiage as what is being used already. We will present this to individuals, institutions (banks, non profits), and to Registered Investment Advisors that have client money to place.

Target Market(s)

High net worth individuals, high income earners, doctors, lawyers, business owners, sophisticated investors

Industry/Entity Type

Investment Advisory

Other font styles liked:
• font that is in logo

Requirements
Must have
• a very simple, but professional, elegant design. must include our color scheme, feel free to add other shades in our scheme.

```html
<!DOCTYPE html>
<html lang="en">
<head>
<meta charset="UTF-8">
<title>Management Team Overview</title>
<link href="https://fonts.googleapis.com/css2?family=Montserrat:wght@300;400;700&display=swap" rel="stylesheet">
<style>
  :root {
    --navy: #053a57;
    --ice: #9dbccb;
    --white: #ffffff;
    --photo-light: #8fa9a8;
    --photo-mid: #3e5d6e;
    --photo-dark: #0c2638;
  }
  * { margin: 0; padding: 0; box-sizing: border-box; }
  html, body { width: 1200px; height: 675px; overflow: hidden; background: var(--navy); }
  .slide {
    position: relative;
    width: 1200px;
    height: 675px;
    background: var(--navy);
    font-family: "Montserrat", Arial, sans-serif;
    overflow: hidden;
  }
  .slide-art { position: absolute; inset: 0; }
  .team-block {
    position: absolute;
    right: 69px;
    top: 68px;
    text-align: right;
    color: var(--white);
  }
  .team-title {
    font-weight: 700;
    font-size: 36px;
    line-height: 1;
    color: var(--ice);
    letter-spacing: 0.2px;
  }
  .team-subtitle {
    margin-top: 18px;
    font-weight: 400;
    font-size: 24px;
    line-height: 1;
    letter-spacing: 0.4px;
  }
  .team-names {
    margin-top: 48px;
    list-style: none;
    font-weight: 300;
    font-size: 24px;
    line-height: 37px;
    letter-spacing: 0.8px;
  }
  .section-label {
    position: absolute;
    left: 66px;
    top: 530px;
    font-weight: 700;
    font-size: 63px;
    line-height: 1;
    color: var(--white);
    letter-spacing: 3px;
  }
</style>
</head>
<body>
  <main class="slide">
    <svg class="slide-art" width="1200" height="675" viewBox="0 0 1200 675">
      <defs>
        <linearGradient id="cityTone" x1="0" y1="0" x2="0.6" y2="1">
          <stop offset="0" stop-color="var(--photo-mid)"/>
          <stop offset="0.45" stop-color="var(--photo-light)"/>
          <stop offset="1" stop-color="var(--photo-dark)"/>
        </linearGradient>
      </defs>
      <polygon class="city-photo" role="img" aria-label="Upward view of tall city office towers with trees, tinted blue"
               points="0,0 153,0 825,675 0,675" fill="url(#cityTone)"/>
      <line class="accent-line" x1="244" y1="0" x2="506" y2="260" stroke="var(--white)" stroke-width="3"/>
      <polygon class="accent-triangle" points="1130,507 1200,578 1200,675 962,675" fill="var(--ice)"/>
    </svg>

    <section class="team-block">
      <h1 class="team-title">MANAGEMENT TEAM</h1>
      <p class="team-subtitle">Veteran Business Owners &amp; Portfolio Manager</p>
      <ul class="team-names">
        <li>DANIEL R. WHITCOMBE</li>
        <li>ELLIOT K. MARSH</li>
      </ul>
    </section>

    <h2 class="section-label">Overview</h2>
  </main>
</body>
</html>
```